Broschüre im Bereich Steuerberatung
Zielgruppe
Steuerberatung
Aufgabenstellung
Die Seite 1 wäre eigentlich fertig, natürlich bin ich offen für Optimierungen. Die weiteren fünf Seiten gilt es noch zu gestalten:
Seite 1
Buchhaltung
Lohnwesen
Steuern
Firmengründung
Kontakt

```html
<!DOCTYPE html>
<html lang="de">
<head>
<meta charset="utf-8">
<title>Varden Treuhand – Broschüre</title>
<link rel="stylesheet" href="https://fonts.googleapis.com/css2?family=Oswald:wght@400;500&family=PT+Serif:ital,wght@0,400;1,400&family=Mulish:wght@400;600;800&display=swap">
<style>
:root{
  --navy:#1f3f7d;
  --orange:#e8561c;
  --green:#9db53b;
  --ink:#3a3a3a;
  --stage:#dbdad3;
  --paper:#ffffff;
}
*{margin:0;padding:0;box-sizing:border-box}
html,body{width:878px;height:1200px;overflow:hidden;background:var(--stage)}
body{position:relative;font-family:"Mulish",sans-serif}
.page{position:absolute;width:370px;height:261px;background:var(--paper);overflow:hidden}
.kicker{position:absolute;left:15px;top:33px;font:400 8.6px/1 "Oswald",sans-serif;letter-spacing:2.3px;color:var(--navy);white-space:nowrap}
.kicker .sep{display:inline-block;width:4px;height:4px;border-radius:50%;background:var(--orange);margin:0 3px 1px 1px;vertical-align:middle}
.photo{position:absolute;left:15px;top:52px;width:177px;height:176px}
.photo.city{background:linear-gradient(180deg,#a18aa6 0%,#7d8a86 40%,#6b7b57 70%,#8a7560 100%)}
.photo.tower{background:linear-gradient(160deg,#4f76b0 0%,#8aa0b8 35%,#a49a5c 65%,#c6862f 100%)}
.photo.glass{background:linear-gradient(170deg,#3f6ea8 0%,#6b8ea0 45%,#6f8a4d 75%,#93a07a 100%)}
.photo.street{background:linear-gradient(180deg,#b67f66 0%,#8e8670 40%,#5f7a4f 70%,#8b8478 100%)}
.photo.avenue{background:linear-gradient(180deg,#9d7ea8 0%,#a48272 40%,#70774a 70%,#8a6a5a 100%)}
.hero{position:absolute;right:8px;font-family:"PT Serif",serif;color:#fff;text-align:right;line-height:.86}
.hero-sub{position:absolute;right:33px;top:44px;font:400 5px/1.4 "Mulish",sans-serif;letter-spacing:2.5px;color:rgba(255,255,255,.8);text-align:left}
.url{position:absolute;left:103px;bottom:10px;font:800 5.6px "Mulish",sans-serif;color:var(--orange)}
.title{position:absolute;left:200px;top:51px;width:160px;font:800 5.6px/1.35 "Mulish",sans-serif;color:var(--navy)}
.lead{display:block;margin-top:2px;font-size:4.1px;color:var(--orange)}
.copy{position:absolute;font:400 3.35px/1.5 "Mulish",sans-serif;color:var(--ink);text-align:justify}
.copy p+p{margin-top:3.4px}
.section-head{font:800 5.2px/1 "Mulish",sans-serif;color:var(--navy);letter-spacing:.2px;margin-bottom:2px;text-align:left}
.portrait{position:absolute;left:282px;top:71px;width:74px;height:51px;background:linear-gradient(90deg,#e8e8e6,#d5d2cc 50%,#ecebe8)}
.calc{position:absolute;width:46px;height:46px;border-radius:50%;background:var(--green);border:2px solid #fff}
.calc svg{position:absolute;left:12px;top:12px}
.pricer{position:absolute;font:800 4.1px/1.35 "Mulish",sans-serif;color:var(--orange)}
.bullet{position:absolute;left:282px;width:62px;font:800 3.5px/1.45 "Mulish",sans-serif;color:#2a5ab5;text-align:justify;padding-left:12px}
.bullet svg{position:absolute;left:0;top:0}
.steps{position:absolute;left:326px;top:82px;width:40px;text-align:center}
.step{height:35px;font:800 3.5px/1.3 "Mulish",sans-serif;color:var(--navy)}
.step svg{display:block;margin:0 auto 2px}
.promo{position:absolute;font:800 5.4px/1.35 "Mulish",sans-serif;color:var(--navy)}
.promo em{font:italic 400 5.6px/1.35 "PT Serif",serif}
.offer{position:absolute;top:145px;width:54px;height:85px;background:#fff;border-radius:4px;box-shadow:0 1px 5px rgba(0,0,0,.18);padding:6px 4px;text-align:center}
.offer h4{font:800 3.6px/1.3 "Mulish",sans-serif;color:var(--navy)}
.offer .price{font:800 3.8px "Mulish",sans-serif;color:var(--orange);margin-bottom:4px}
.offer ul{list-style:none;text-align:left;font:400 2.2px/1.4 "Mulish",sans-serif;color:#555}
.offer li{margin-bottom:2.5px;padding-left:4px;position:relative}
.offer li::before{content:"✓";position:absolute;left:0;color:var(--orange)}
.offer .fee{text-align:left;font-size:2px;color:#888;margin-top:3px}
.offer .cta{position:absolute;left:8px;right:8px;bottom:6px;height:9px;border-radius:5px;background:var(--green);font:600 2.4px/9px "Mulish",sans-serif;color:#fff}
.brand{position:absolute;font:400 15px/1 "PT Serif",serif;color:var(--navy)}
.brand .mark{display:inline-block;width:7px;height:7px;border-radius:50%;background:var(--orange);margin-left:2px;vertical-align:middle}
.brand-sub{position:absolute;font:400 2.9px/1.4 "Mulish",sans-serif;letter-spacing:1.3px;color:#888;text-align:center}
.address{position:absolute;font:400 3.9px/1.6 "Mulish",sans-serif;color:var(--ink)}
.address .o{color:var(--orange)}
.map{position:absolute;width:92px;height:106px;background:linear-gradient(135deg,#f6f7fa,#e6eaf2)}
.divider{position:absolute;left:184px;top:120px;width:.6px;height:108px;background:var(--navy)}
</style>
</head>
<body>

<!-- Seite 1 -->
<section class="page" style="left:47px;top:46px">
  <div class="kicker">STEUERN<span class="sep"></span>MEHRWERT<span class="sep"></span>TREUHAND<span class="sep"></span></div>
  <div class="photo city" role="img" aria-label="Foto einer Geschäftsstrasse mit Hochhäusern und Bäumen">
    <div class="hero" style="top:12px;font-size:31px">varden</div>
    <div class="hero-sub">TREUHAND<br>CONSULTING</div>
    <div class="url">vardentreuhand.ch</div>
  </div>
  <h2 class="title">Zuverlässig und partnerschaftlich:<br>Ihre massgeschneiderten Treuhand-Lösungen</h2>
  <div class="copy" style="left:200px;top:71px;width:73px">
    <p>Sie möchten Ihre Steuern, Ihre Buchhaltung oder Ihr Lohnwesen in verlässliche Hände geben? Sie legen Wert auf eine persönliche Betreuung mit gleichbleibendem Ansprechpartner, auf individuelle Strategien und auf ein angenehmes Miteinander?</p>
    <p>Dann freue ich mich auf Ihre Kontaktaufnahme.</p>
  </div>
  <div class="portrait" role="img" aria-label="Porträtfoto der Inhaberin"></div>
  <div class="copy" style="left:200px;top:140px;width:73px">
    <div class="section-head">BUCHHALTUNG</div>
    <p>Buchhaltung ist komplex und aufwendig – das kostet Unternehmer viel Zeit, die sie anderswo wertschöpfend einsetzen könnten. Mithilfe moderner Hilfsmittel und bewährter Prozesse entlaste ich Sie zuverlässig und zum Fixpreis.</p>
  </div>
  <div class="copy" style="left:282px;top:140px;width:74px">
    <div class="section-head">STEUERERKLÄRUNG</div>
    <p>Jeder möchte seine Steuerlast optimieren, nur wenige setzen sich aktiv damit auseinander. Denn das kostet Zeit und verlangt nach umfangreichem Wissen. Vertrauen Sie mir Ihre Steuererklärungen an – und holen Sie sich zurück, was Ihnen zusteht.</p>
  </div>
  <div class="copy" style="left:200px;top:190px;width:73px">
    <div class="section-head">LOHNWESEN</div>
    <p>Entscheiden Sie selbst, in welcher Form Sie auf meine Expertise zugreifen, um sich beim Thema Lohnbuchhaltung zu entlasten.</p>
  </div>
  <div class="copy" style="left:282px;top:190px;width:74px">
    <div class="section-head">FIRMENGRÜNDUNG</div>
    <p>Gründen Sie Ihre Schweizer Gesellschaft schnell und sicher. Mit meiner langjährigen Erfahrung, meinem Wissen und meiner Zusammenarbeit mit einem versierten Notar unterstütze ich Sie zuverlässig – auch über Ihre Gründung hinaus.</p>
  </div>
</section>

<!-- Seite 2 Buchhaltung -->
<section class="page" style="left:452px;top:46px">
  <div class="kicker">ADDITION<span class="sep"></span>SUBTRAKTION<span class="sep"></span>ERFOLG<span class="sep"></span></div>
  <div class="photo tower" role="img" aria-label="Foto eines gläsernen Hochhauses hinter Baumkronen"></div>
  <div class="hero" style="right:178px;top:60px;font-size:38px;right:auto;left:30px;width:160px">buch-<br>haltung</div>
  <h2 class="title">Buchhaltung kostet Sie viel Zeit<br>– Ich gebe Sie Ihnen zurück<span class="lead">Ich übernehme Ihre Buchhaltung –<br>akribisch, verlässlich, verantwortungsvoll</span></h2>
  <div class="copy" style="left:200px;top:90px;width:72px">
    <p>Unternehmer zählen die Buchhaltung in der Regel nicht zu ihren Leidenschaften.</p>
    <p>Und dennoch ist eine ordentliche Buchhaltung das Rückgrat eines jeden erfolgreichen Betriebs. Es ergibt also durchaus Sinn, hierfür ausreichend Ressourcen bereit zu stellen – jedoch nicht die eigenen.</p>
    <p>Wenn Sie selbst oder Ihre Mitarbeiter sich um dieses komplexe „Pflichtthema“ kümmern, bleiben andere, wertschöpfende Tätigkeiten auf der Strecke: neue Kunden akquirieren, Produkte weiterentwickeln, Services ausbauen usw.</p>
  </div>
  <div class="copy" style="left:282px;top:90px;width:74px">
    <p>Die Folge: Es kommt zu unnötigem Mehraufwand und die Entwicklung Ihres Unternehmens schreitet langsamer voran als geplant.</p>
    <p>Beides ist unschön – und beides lässt sich leicht vermeiden. Nutzen Sie Ihre wertvolle Zeit lieber gewinnbringend und überlassen Sie Ihre Buchhaltung einem Profi.</p>
    <p>Mit viel Erfahrung, Wissen und Leidenschaft kümmere ich mich um Ihre Geschäftsvorfälle, während Ihr Team und Sie sich auf Ihre Kerntätigkeit fokussieren.</p>
  </div>
  <div class="calc" style="left:167px;top:187px"><svg width="22" height="22" viewBox="0 0 22 22" fill="none" stroke="#fff" stroke-width="1.6"><rect x="1" y="1" width="20" height="20" rx="2"/><path d="M4 6h5M13 4l4 4M17 4l-4 4M4 15h5M6.5 12.5v5M13 14h4M13 17h4"/></svg></div>
  <div class="pricer" style="left:224px;top:205px">Mit individuellem Preisrechner auf:<br>www.vardentreuhand.ch/treuhand/buchhaltung</div>
</section>

<!-- Seite 3 Lohnwesen -->
<section class="page" style="left:47px;top:330px">
  <div class="kicker">IHRE ZUKUNFT<span class="sep"></span>MEHR<span class="sep"></span>LOHN<span class="sep"></span></div>
  <div class="photo glass" role="img" aria-label="Foto einer Glasfassade mit Bäumen davor"></div>
  <div class="hero" style="left:20px;top:63px;width:166px;font-size:38px">lohn-<br>wesen</div>
  <h2 class="title">Lohnbuchhaltung ohne Stress:<br>So gewinnen Sie mehr Zeit<span class="lead">Ich erledige Ihr Lohnwesen – präzise, sicher, zuverlässig</span></h2>
  <div class="copy" style="left:200px;top:84px;width:72px">
    <p>Sicherlich stimmen Sie mir zu, wenn ich das Personalwesen und die Saläradministration zu den sensiblen Bereichen Ihres Unternehmens zähle. Schliesslich erwarten Ihre Mitarbeiter, dass ihre Gehälter pünktlich auf dem Konto eingehen.</p>
    <p>Doch die Lohnbuchhaltung ist komplex und daher zeitaufwendig – sie bindet wertvolle Ressourcen, die Ihnen für andere, wert schöpfen de Tätigkeiten fehlen.</p>
    <p>Holen Sie sich die Zeit zurück und legen Sie Ihre Lohnbuchhaltung in meine Hände. Dabei haben Sie die Wahl zwischen Optimierung und Outsourcing.</p>
  </div>
  <div class="bullet" style="top:84px;left:282px;width:78px"><svg width="8" height="8" viewBox="0 0 8 8"><circle cx="4" cy="4" r="4" fill="#e8561c"/><path d="M2 4h4M4.3 2.3 6 4 4.3 5.7" stroke="#fff" stroke-width=".8" fill="none"/></svg>Sie übernehmen die vorbereitenden Arbeiten, während ich mich um die Umsetzung kümmere. So optimieren wir gemeinsam Ihre Vorgänge und entlasten Ihre interne Buchhaltung.</div>
  <div class="bullet" style="top:125px;left:282px;width:78px"><svg width="8" height="8" viewBox="0 0 8 8"><circle cx="4" cy="4" r="4" fill="#e8561c"/><path d="M2 4h4M4.3 2.3 6 4 4.3 5.7" stroke="#fff" stroke-width=".8" fill="none"/></svg>Sie lagern Ihre Lohnbuchhaltung an mich aus. Insbesondere kleine und mittlere Unternehmen profitieren vom Outsourcing immens, da sie sich von diesem Thema komplett befreien.</div>
</section>

<!-- Seite 4 Steuern -->
<section class="page" style="left:452px;top:330px">
  <div class="kicker">ERFOLG LÄSST SICH STEUERN<span class="sep"></span></div>
  <div class="photo street" role="img" aria-label="Foto einer baumgesäumten Stadtstrasse"></div>
  <div class="hero" style="left:20px;top:62px;width:166px;font-size:34px">steuern</div>
  <h2 class="title">Professionell und transparent:<br>Ihre Steuererklärung und Steuerberatung<span class="lead">Ich kümmere mich persönlich um Ihre Steuerangelegenheiten</span></h2>
  <div class="copy" style="left:200px;top:84px;width:101px">
    <p>Steuern sind ein sensibles Thema – schliesslich geht es um Ihr Geld. Setzen Sie gleich auf professionelle Unterstützung: Vermeiden Sie teure Fehler, sparen Sie viel Zeit und schonen Sie Ihre Nerven.</p>
    <div class="section-head" style="margin-top:5px">FÜR PRIVATPERSONEN</div>
    <p>Weshalb ich mir viel Zeit für Sie nehme und Sie individuell betreue? Weil wir mit Konzepten „von der Stange“ bei Ihrer Steuererklärung nicht weit kommen.</p>
    <p>Hingegen habe ich die Abläufe rund um Ihre Steuerberatung standardisiert – um es Ihnen einfach zu machen: Wir tauschen uns per E-Mail, Telefon, Videocall oder per Post aus. So erhalten Sie schnelle Ergebnisse und sparen sich Weg und Kosten für einen persönlichen Termin.</p>
  </div>
  <div class="steps">
    <div class="step"><svg width="16" height="16" viewBox="0 0 16 16" fill="none" stroke="#1f3f7d" stroke-width=".9"><rect x="2" y="2" width="10" height="12"/><path d="M4 6h6M4 9h4M8 12l6-7"/></svg>Checkliste<br>ausfüllen</div>
    <div class="step"><svg width="16" height="16" viewBox="0 0 16 16" fill="none" stroke="#1f3f7d" stroke-width=".9"><rect x="4" y="1" width="9" height="11"/><path d="M6 4h5M6 7h5M1 12h14v2H1z"/></svg>Unterlagen<br>bereitstellen</div>
    <div class="step"><svg width="16" height="16" viewBox="0 0 16 16" fill="none" stroke="#1f3f7d" stroke-width=".9"><rect x="2" y="4" width="12" height="9"/><path d="M2 4l6 5 6-5"/></svg>Unterlagen<br>übergeben</div>
    <div class="step"><svg width="16" height="16" viewBox="0 0 16 16" fill="none" stroke="#1f3f7d" stroke-width=".9"><rect x="3" y="1" width="10" height="14"/><path d="M5 7h6M5 10h6M5 13h4"/><text x="8" y="5" font-size="3.2" text-anchor="middle" fill="#1f3f7d" stroke="none" font-family="Mulish">TAX</text></svg>Meine<br>Arbeit</div>
    <div class="step"><svg width="16" height="16" viewBox="0 0 16 16" fill="none" stroke="#1f3f7d" stroke-width=".9"><path d="M3 1h7l3 3v11H3z"/><path d="M8 13V6M5.5 8.5 8 6l2.5 2.5"/></svg>Unterschreiben<br>+ Abgeben</div>
  </div>
  <div class="calc" style="left:167px;top:187px"><svg width="22" height="22" viewBox="0 0 22 22" fill="none" stroke="#fff" stroke-width="1.6"><rect x="1" y="1" width="20" height="20" rx="2"/><path d="M4 6h5M13 4l4 4M17 4l-4 4M4 15h5M6.5 12.5v5M13 14h4M13 17h4"/></svg></div>
  <div class="pricer" style="left:222px;top:192px">Mit individuellem Preisrechner auf:<br>www.vardentreuhand.ch/steuererklaerung</div>
</section>

<!-- Seite 5 Firmengründung -->
<section class="page" style="left:47px;top:621px">
  <div class="kicker">DON'T DREAM IT.<span class="sep"></span>DO IT!<span class="sep"></span></div>
  <div class="photo avenue" role="img" aria-label="Foto einer Häuserzeile mit Bäumen und Velos"></div>
  <div class="hero" style="left:15px;top:62px;width:172px;font-size:36px">firmen-<br>gründung</div>
  <h2 class="title">Varden Treuhand:<br>Professionelle Unternehmensgründung mit System<span class="lead">Varden Treuhand - Ihr kompetenter Partner</span></h2>
  <div class="copy" style="left:200px;top:84px;width:72px">
    <p>Die Unternehmensgründung gehört zu den emotionalsten Erlebnissen in der Karriere. Gut, wenn man hierbei einen verlässlichen Partner hat, der einen kühlen Kopf bewahrt und sich bis ins Detail mit sämtlichen Anforderungen auskennt.</p>
  </div>
  <div class="copy" style="left:282px;top:84px;width:74px">
    <p>Schon seit mehr als 13 Jahren unterstütze ich Start-ups auf ihrem Weg an die Spitze – vom ersten Tag an rund um die Gründung und danach bei der Buchhaltung, im Lohnwesen und bei den Steuern.</p>
  </div>
  <div class="promo" style="left:200px;top:129px">Kompetenter Service. <em>Komplett ohne<br>persönlichen Notartermin.</em></div>
  <div class="offer" style="left:248px">
    <h4>FULLSERVICE-PAKET<br>GRÜNDUNG</h4>
    <div class="price">CHF 750.-</div>
    <ul><li>Telefonische Beratung</li><li>Erstellen der Gründungsdokumente</li><li>Vertretung beim Notar durch Vollmacht</li><li>Anmeldung beim Handelsregisteramt</li></ul>
    <div class="fee">exkl. HR-Gebühren</div>
    <div class="cta">JETZT GRÜNDEN ›</div>
  </div>
</section>

<!-- Seite 6 Firmengründung Variante -->
<section class="page" style="left:452px;top:621px">
  <div class="kicker">DON'T DREAM IT.<span class="sep"></span>DO IT!<span class="sep"></span></div>
  <div class="photo avenue" role="img" aria-label="Foto einer Häuserzeile mit Bäumen und Velos"></div>
  <div class="hero" style="left:15px;top:62px;width:172px;font-size:36px">firmen-<br>gründung</div>
  <h2 class="title">Varden Treuhand:<br>Professionelle Unternehmensgründung mit System<span class="lead">Varden Treuhand - Ihr kompetenter Partner</span></h2>
  <div class="copy" style="left:200px;top:84px;width:72px">
    <p>Die Unternehmensgründung gehört zu den emotionalsten Erlebnissen in der Karriere. Gut, wenn man hierbei einen verlässlichen Partner hat, der einen kühlen Kopf bewahrt und sich bis ins Detail mit sämtlichen Anforderungen auskennt.</p>
  </div>
  <div class="copy" style="left:282px;top:84px;width:74px">
    <p>Schon seit mehr als 13 Jahren unterstütze ich Start-ups auf ihrem Weg an die Spitze – vom ersten Tag an rund um die Gründung und danach bei der Buchhaltung, im Lohnwesen und bei den Steuern.</p>
  </div>
  <div class="promo" style="left:200px;top:147px">Kompetenter Service.<br><em>Komplett ohne<br>persönlichen Notartermin.</em></div>
  <div class="offer" style="left:283px">
    <h4>FULLSERVICE-PAKET<br>GRÜNDUNG</h4>
    <div class="price">CHF 750.-</div>
    <ul><li>Telefonische Beratung</li><li>Erstellen der Gründungsdokumente</li><li>Vertretung beim Notar durch Vollmacht</li><li>Anmeldung beim Handelsregisteramt</li></ul>
    <div class="fee">exkl. HR-Gebühren</div>
    <div class="cta">JETZT GRÜNDEN ›</div>
  </div>
</section>

<!-- Seite 7 Kontakt -->
<section class="page" style="left:47px;top:907px">
  <h2 class="title" style="left:15px;top:53px;width:200px">Zuverlässig und partnerschaftlich:<br>Ihre massgeschneiderten Treuhand-Lösungen<span class="lead">Sie haben noch Fragen? Rufen Sie uns an oder senden<br>Sie uns eine Mail, wir helfen Ihnen gerne weiter.</span></h2>

  <div class="brand" style="left:15px;top:132px">varden<span class="mark"></span></div>
  <div class="brand-sub" style="left:15px;top:150px;width:50px">TREUHAND<br>CONSULTING</div>
  <div class="address" style="left:15px;top:166px">
    <span class="o">Varden Treuhand Consulting GmbH<br>Lindenweg 14<br>6004 Seestadt</span><br>+41 (0) 41 555 01 10<br>+41 (0)79 555 02 20 Mobile<br>info@vardentreuhand.ch
  </div>
  <div class="map" style="left:82px;top:122px" role="img" aria-label="Lageplan des Standorts Seestadt"></div>

  <div class="divider"></div>

  <div class="brand" style="left:197px;top:132px">varden<span class="mark"></span></div>
  <div class="brand-sub" style="left:197px;top:150px;width:50px">TREUHAND<br>CONSULTING</div>
  <div class="address" style="left:197px;top:166px">
    <span class="o">Varden Treuhand Consulting GmbH<br>Birkenrain 22<br>8812 Uferdorf</span><br>+41 (0) 41 555 01 10<br>+41 (0)79 555 02 20 Mobile<br>info@vardentreuhand.ch
  </div>
  <div class="map" style="left:262px;top:122px" role="img" aria-label="Lageplan des Standorts Uferdorf"></div>
</section>

</body>
</html>
```